Etiketten Fine-Tuning für Creatine Supplement
Zielgruppe
Bitte auf www.kelvora-vital.example hereinschauen.
Please check our webpage: www.kelvora-vital.example
Aufgabenstellung
Eine Vorlage besteht sowie ein Design Guide.
Das bestehende Etikett soll den letzten Feinschliff bekommen um den Kunden optisch zum Kauf anzuregen.
Das Design soll eindeutlich wiedererkennbar sein, große Änderungen sind nicht nötig. Ein minimalistischer Ansatz kann auch gewählt werden.
Weitere Produkte findet ihr auf der Homepage oder auf Zolvex unter dem Begriff Kelvora Vital.
Das Format sollte im Photoshop sein oder irgendwie dort editierbar sein da ich kein Illustrator habe.
Das Etikett muss einen 2 mm Rand für den Zuschnitt haben. Minimale Schriftgrösse ist 1.2mm
Etikettengrösse: 75 x210mm
Die Texte sind verbindlich und müssen verbleiben.
Alle Fonts sind in den Dateien.
A template exists as well as a design guide.
The existing label is to be given the final touches in order to visually encourage the customer to buy.
The design should be clearly recognizable, large changes are not necessary. A minimalist approach can also be chosen.
You can find more products on the homepage or on Zolvex under the term Kelvora Vital.
The format must be in Photoshop. The label must have a 2 mm margin for cutting.
Label size: 75 x210mm
The texts are legally binding and must remain so.

```html
<!DOCTYPE html>
<html lang="de">
<head>
<meta charset="utf-8">
<title>Kelvora Creatine+ Etikett</title>
<link rel="stylesheet" href="https://fonts.googleapis.com/css2?family=Montserrat:wght@200;300;400;700;800&display=swap">
<style>
  :root {
    --page: #ffffff;
    --green-deep: #178a32;
    --green-main: #22a03c;
    --green-light: #6cc35a;
    --white: #ffffff;
    --ink-green: #1c8a35;
  }
  html, body {
    margin: 0;
    padding: 0;
    width: 1200px;
    height: 1200px;
    overflow: hidden;
    background: var(--page);
  }
  .canvas {
    position: relative;
    width: 1200px;
    height: 1200px;
  }
  .label {
    position: absolute;
    left: 220px;
    top: 125px;
    width: 760px;
    height: 950px;
    display: block;
  }
  .label text {
    font-family: "Montserrat", sans-serif;
    fill: var(--white);
  }
  .brand-word { font-weight: 800; font-size: 92px; letter-spacing: 2px; }
  .product-word { font-weight: 200; font-size: 92px; letter-spacing: 2px; }
  .logo-name { font-weight: 700; font-size: 27px; }
  .category-tag { font-weight: 700; font-size: 20px; fill: var(--ink-green) !important; }
  .claim { font-weight: 400; font-size: 47px; }
  .count-strong { font-weight: 700; font-size: 28px; }
  .count-light { font-weight: 300; font-size: 28px; }
</style>
</head>
<body>
<div class="canvas">
  <svg class="label" viewBox="0 0 760 950" xmlns="http://www.w3.org/2000/svg">
    <defs>
      <linearGradient id="label-base" x1="0" y1="0" x2="1" y2="1">
        <stop offset="0" stop-color="#2ea843"/>
        <stop offset="0.55" stop-color="#1f9a3a"/>
        <stop offset="1" stop-color="#178a32"/>
      </linearGradient>
      <radialGradient id="label-glow" cx="0.62" cy="0.42" r="0.55">
        <stop offset="0" stop-color="#7fcb6a" stop-opacity="0.55"/>
        <stop offset="1" stop-color="#7fcb6a" stop-opacity="0"/>
      </radialGradient>
    </defs>

    <g class="label-background">
      <rect width="760" height="950" fill="url(#label-base)"/>
      <rect width="760" height="950" fill="url(#label-glow)" role="img" aria-label="Dekoratives Rautenmuster in hell- und dunkelgrünen Tönen"/>
    </g>

    <g class="divider-lines" stroke="var(--white)" stroke-width="3">
      <line x1="355" y1="0" x2="355" y2="89"/>
      <line x1="355" y1="820" x2="355" y2="950"/>
    </g>

    <g class="brand-mark">
      <circle cx="209" cy="137" r="86" fill="none" stroke="var(--white)" stroke-width="12"/>
      <text class="logo-name" x="209" y="131" text-anchor="middle">Kelvora</text>
      <text class="logo-name" x="209" y="164" text-anchor="middle">Vital</text>
    </g>

    <g class="product-name">
      <text class="brand-word" transform="translate(190 895) rotate(-90)">KELVORA</text>
      <text class="product-word" transform="translate(282 895) rotate(-90)">CREATINE+</text>
    </g>

    <g class="category">
      <rect x="355" y="145" width="333" height="46" fill="var(--white)"/>
      <text class="category-tag" x="371" y="175">Nahrungsergänzungsmittel</text>
    </g>

    <g class="claims">
      <text class="claim" x="355" y="250">Mit Creatine</text>
      <text class="claim" x="355" y="310">Monohydrate,</text>
      <text class="claim" x="355" y="370">Beta-Alanin</text>
      <text class="claim" x="355" y="430">und D-Ribose</text>
    </g>

    <g class="certificate-badges" fill="var(--white)">
      <circle cx="402" cy="633" r="46"/>
      <polygon points="511,587 551,610 551,656 511,679 471,656 471,610"/>
      <polygon points="611,587 651,610 651,656 611,679 571,656 571,610"/>
    </g>

    <g class="package-count">
      <rect x="358" y="712" width="18" height="62" rx="9" fill="var(--white)"/>
      <text x="393" y="738"><tspan class="count-strong">150</tspan><tspan class="count-light"> Kapseln</tspan></text>
      <text x="393" y="772"><tspan class="count-strong">30</tspan><tspan class="count-light"> Tagesportionen</tspan></text>
    </g>
  </svg>
</div>
</body>
</html>
```